Candle company needs a label for candle

Looking for a designer to create my candle label. I am going to attach a few pictures of my vision for the label as well as my Company Logo and jar I have puchased. I'm going for the modern rustic feel but you are the designer and have full trust in your abilities. The label is going to be printed on Kraft paper (2x3) so looking for the font to be black. The candle label MUST include the following information:
Candle Birchway Co.
NO. 01: Eucalyptus + Spearmint
Handmade In NJ
Soy Wax
9oz

Industry/Entity Type

Candle Industry

Colors

Designer to choose colors to be used in the design.

Requirements
Should not have
• Any images

```html
<!DOCTYPE html>
<html lang="en">
<head>
<meta charset="utf-8">
<title>Candle Birchway Co. — No. 01 Label</title>
<link href="https://fonts.googleapis.com/css2?family=Jura:wght@500;600&display=swap" rel="stylesheet">
<style>
  :root {
    --canvas: #ece7e1;
    --label-light: #ffffff;
    --label-dark: #000000;
    --ink-light: #1c1c1c;
    --ink-dark: #b99b5f;
  }
  * { margin: 0; padding: 0; box-sizing: border-box; }
  html, body {
    width: 1200px;
    height: 1200px;
    overflow: hidden;
  }
  body {
    background: var(--canvas);
    font-family: "Jura", sans-serif;
    position: relative;
  }
  .label-set {
    position: absolute;
    left: 0;
    top: 386px;
    width: 1200px;
    height: 428px;
    display: flex;
  }
  .label {
    position: relative;
    width: 600px;
    height: 428px;
    text-transform: uppercase;
  }
  .label--light { background: var(--label-light); color: var(--ink-light); }
  .label--dark  { background: var(--label-dark);  color: var(--ink-dark); }

  .brand-name {
    position: absolute;
    left: 0;
    width: 600px;
    top: 108px;
    text-align: center;
    font-weight: 500;
    font-size: 24px;
    letter-spacing: 0.18em;
    line-height: 1.35;
  }
  .scent-number {
    position: absolute;
    left: 76px;
    top: 238px;
    font-weight: 500;
    font-size: 14px;
    letter-spacing: 0.08em;
  }
  .scent-name {
    position: absolute;
    left: 76px;
    top: 263px;
    font-weight: 600;
    font-size: 25px;
    letter-spacing: 0.07em;
    white-space: nowrap;
  }
  .rating {
    position: absolute;
    left: 78px;
    top: 313px;
    display: flex;
    gap: 5px;
  }
  .rating span {
    width: 6px;
    height: 6px;
    border-radius: 50%;
    background: currentColor;
  }
  .details {
    position: absolute;
    left: 76px;
    top: 347px;
    font-weight: 600;
    font-size: 15px;
    letter-spacing: 0.1em;
    line-height: 28px;
  }
  .weight {
    position: absolute;
    right: 67px;
    top: 375px;
    font-weight: 600;
    font-size: 15px;
    letter-spacing: 0.08em;
    line-height: 28px;
  }
</style>
</head>
<body>
  <main class="label-set">
    <section class="label label--light">
      <div class="brand-name">Candle Birchway<br>Co.</div>
      <div class="scent-number">No. 01:</div>
      <h1 class="scent-name">Eucalyptus + Spearmint</h1>
      <div class="rating" aria-hidden="true"><span></span><span></span><span></span><span></span><span></span></div>
      <div class="details">Handmade in NJ<br>Soy Wax</div>
      <div class="weight">•9oz</div>
    </section>
    <section class="label label--dark">
      <div class="brand-name">Candle Birchway<br>Co.</div>
      <div class="scent-number">No. 01:</div>
      <h2 class="scent-name">Eucalyptus + Spearmint</h2>
      <div class="rating" aria-hidden="true"><span></span><span></span><span></span><span></span><span></span></div>
      <div class="details">Handmade in NJ<br>Soy Wax</div>
      <div class="weight">•9oz</div>
    </section>
  </main>
</body>
</html>
```